Varga Lillas Physiotherapy Business Card Vienna

We need a business card design for a newly created Physiotherapy company based in Vienna Austria.
We seek a simple, modern, minimalist design without too much color variation. The font should look young/fresh, but definitely not childish or so. Since we are a starting Business, we currently haven't got a logo, if you feel like a logo would fit your design, feel free to use one, but it's not necessary.
Target Market(s)
Healthcare, young and elderly people with mobility issues
Industry/Entity Type
Health And Wellness
Contact Information for Business Card
Name: Lilla Varga
Title description: Physiotherapist
Phone num: +43 664 5290 4816
e-mail: lilla.praxis@brelomail.com
Colors
Designer to choose colors to be used in the design.
Requirements
Must have
- Final design language must be in German, basically, the Title Description needs to be "Physiotherapeutin" the other details remain as in the English Language.
Nice to have
- Simple, modern, minimalist design
Should not have
- too many colors, Obvious use of a skeleton, skull, spline

```html
<!DOCTYPE html>
<html lang="de">
<head>
<meta charset="utf-8">
<title>Lilla Varga – Physiotherapeutin</title>
<link rel="stylesheet" href="https://fonts.googleapis.com/css2?family=Jost:wght@400&display=swap">
<style>
  :root {
    --backdrop: #cacfe3;
    --card: #ecf0f9;
    --ink: #4f5770;
    --label: #a3a3ad;
    --disc: #b0aeb5;
    --disc-edge: #9e9ba2;
    --band-text: #ffffff;
  }
  html, body {
    margin: 0;
    padding: 0;
    width: 1200px;
    height: 880px;
    overflow: hidden;
    background: var(--backdrop);
    font-family: "Jost", sans-serif;
  }
  .business-card {
    position: absolute;
    left: 216px;
    top: 192px;
    width: 768px;
    height: 496px;
    background: var(--card);
    overflow: hidden;
  }
  .corner-disc {
    position: absolute;
    left: 0;
    top: 0;
  }
  .monogram-name {
    position: absolute;
    left: 40px;
    top: 112px;
    width: 150px;
    text-align: center;
    font-size: 22px;
    color: var(--ink);
    margin: 0;
  }
  .identity {
    position: absolute;
    right: 72px;
    top: 54px;
    text-align: right;
    color: var(--ink);
  }
  .identity-name {
    margin: 0;
    font-size: 45px;
    font-weight: 400;
    line-height: 1;
  }
  .identity-title {
    margin: 8px 0 0;
    font-size: 24px;
    line-height: 1;
  }
  .title-bracket {
    position: absolute;
    left: 442px;
    top: 102px;
  }
  .contact-list {
    position: absolute;
    left: 322px;
    top: 288px;
    margin: 0;
    padding: 0;
    list-style: none;
    font-size: 29px;
    color: var(--ink);
  }
  .contact-item {
    display: flex;
    line-height: 44px;
  }
  .contact-label {
    width: 48px;
    color: var(--label);
  }
  .band-shade {
    position: absolute;
    left: 0;
    top: 418px;
    width: 100%;
    height: 21px;
    background: linear-gradient(to bottom, rgba(79,87,112,0), rgba(79,87,112,0.14));
  }
  .location-band {
    position: absolute;
    left: 0;
    top: 439px;
    width: 100%;
    height: 57px;
    background: var(--ink);
    color: var(--band-text);
    font-size: 24px;
    display: flex;
    align-items: center;
    justify-content: center;
  }
</style>
</head>
<body>
  <section class="business-card">
    <svg class="corner-disc" width="340" height="320" viewBox="0 0 340 320" aria-hidden="true">
      <circle cx="0" cy="-4" r="316" fill="var(--disc-edge)"/>
      <circle cx="0" cy="-4" r="296" fill="var(--disc)"/>
    </svg>
    <p class="monogram-name">Lilla Varga</p>

    <header class="identity">
      <h1 class="identity-name">Lilla Varga</h1>
      <p class="identity-title">Physiotherapeutin</p>
    </header>
    <svg class="title-bracket" width="70" height="60" viewBox="0 0 70 60" aria-hidden="true">
      <polyline points="1.5,0 1.5,55 70,55" fill="none" stroke="var(--ink)" stroke-width="2.5"/>
    </svg>

    <ul class="contact-list">
      <li class="contact-item"><span class="contact-label">T:</span><span>43.664.5290.4816</span></li>
      <li class="contact-item"><span class="contact-label">E:</span><span>lilla.praxis@brelomail.com</span></li>
    </ul>

    <div class="band-shade"></div>
    <footer class="location-band">Vienna Austria</footer>
  </section>
</body>
</html>
```